PowerPoint Presentation Design < 10 Slides

Would like to update the following presentation to have a consistent theme and organization of the content. Following tolvenbrook.com or Quillmarsh4040.com.

Speaking at a conference would like to have a great public facing design!

Target Market(s)

Postal and parcel delivery industry

Colors
3176b5

Requirements
Must have
• Modern and consistent theme.
• Professional, Business focused.
Nice to have
• Engaging and thought provoking.

```html
<!DOCTYPE html>
<html lang="en">
<head>
<meta charset="utf-8">
<title>Conference Deck – Slides 7 to 9</title>
<link href="https://fonts.googleapis.com/css2?family=Arimo:wght@400;700&display=swap" rel="stylesheet">
<style>
:root{
  --blue:#3176b5;
  --navy:#25527f;
  --ink:#222;
  --panel:#f0f0f0;
  --rule:#3176b5;
  --white:#fff;
}
*{margin:0;padding:0;box-sizing:border-box}
html,body{width:1200px;height:1200px;overflow:hidden;background:var(--white)}
body{position:relative;font-family:"Arimo",Arial,sans-serif;color:var(--ink)}
.slide{position:absolute;width:571px;height:320px;background:var(--white)}
.slide-7{left:24px;top:41px}
.slide-8{left:612px;top:41px}
.slide-9{left:24px;top:384px}
.slide-title{position:absolute;left:18px;top:18px;font-size:21px;font-weight:400;color:var(--ink);letter-spacing:-.2px}
.slide-title strong{color:var(--blue);font-weight:700}
.footer{position:absolute;left:0;right:0;bottom:0;height:22px;background:var(--navy);border-top:2px solid var(--blue);color:var(--white);font-size:5px;display:flex;align-items:center;justify-content:space-between;padding:0 22px 0 18px}

/* slide 7 */
.expectations{position:absolute;left:18px;top:58px;list-style:none}
.expectations li{position:absolute;left:0;display:flex;gap:9px;width:290px}
.expectations svg{flex:none;width:15px;height:15px;margin-top:-1px}
.expectations b{display:block;font-size:12.5px;font-weight:700}
.expectations span{display:block;font-size:10.5px;margin-top:1px}
.target-photo{position:absolute;left:310px;top:0;width:261px;height:298px;background:linear-gradient(160deg,#c7d5e2 0%,#8ea6bd 40%,#4e5f78 75%,#7f8da0 100%)}

/* slide 8 */
.pillars{position:absolute;left:18px;top:62px;display:flex;gap:8px}
.pillar{width:101px}
.pillar-icon{height:50px;display:flex;justify-content:center;align-items:flex-start;margin-bottom:11px}
.pillar-icon svg{width:44px;height:44px}
.pillar-card{background:var(--panel);height:155px;padding:10px 7px 0}
.pillar-card h3{font-size:10.5px;font-weight:700;text-align:center;height:26px;display:flex;align-items:center;justify-content:center;line-height:1.2;border-bottom:1px solid var(--rule);padding-bottom:0;margin-bottom:10px;height:35px}
.pillar-card ul{list-style:none;font-size:9px;line-height:1.22}
.pillar-card li{position:relative;padding-left:7px;margin-bottom:5px}
.pillar-card li::before{content:"•";position:absolute;left:0;color:var(--blue)}

/* slide 9 */
.locker-photo{position:absolute;left:0;top:50px;width:571px;height:110px;background:linear-gradient(90deg,#c9c5cf 0%,#a994c6 20%,#5fb7c2 45%,#7fae4f 70%,#a994c6 100%)}
.thoughts{position:absolute;top:172px;left:0;width:571px;height:97px}
.thought{position:absolute;top:0;text-align:center;font-size:12.5px;font-weight:700;line-height:1.2}
.thought svg{display:block;margin:0 auto 8px;width:48px;height:48px}
.divider{position:absolute;top:0;width:1px;height:97px;background:#ddd}
.credits{position:absolute;left:18px;top:280px;font-size:5.5px;color:#666;line-height:1.05}
.credits a{color:#666}

.part-heading{position:absolute;left:26px;top:1080px;font-size:76px;font-weight:400;color:#000;letter-spacing:-.5px}
</style>
</head>
<body>

<section class="slide slide-7">
  <h2 class="slide-title">Customer <strong>Expectations</strong></h2>
  <ul class="expectations">
    <li style="top:0"><svg viewBox="0 0 16 16"><circle cx="8" cy="8" r="7" fill="none" stroke="#3176b5" stroke-width="1"/><path d="M4.8 8.2l2.2 2.2 4.2-4.4" fill="none" stroke="#3176b5" stroke-width="1"/></svg><div><b>Intimate unified experience</b></div></li>
    <li style="top:31px"><svg viewBox="0 0 16 16"><circle cx="8" cy="8" r="7" fill="none" stroke="#3176b5" stroke-width="1"/><path d="M4.8 8.2l2.2 2.2 4.2-4.4" fill="none" stroke="#3176b5" stroke-width="1"/></svg><div><b>Convenience</b></div></li>
    <li style="top:61px"><svg viewBox="0 0 16 16"><circle cx="8" cy="8" r="7" fill="none" stroke="#3176b5" stroke-width="1"/><path d="M4.8 8.2l2.2 2.2 4.2-4.4" fill="none" stroke="#3176b5" stroke-width="1"/></svg><div><b>Flexibility</b></div></li>
    <li style="top:89px"><svg viewBox="0 0 16 16"><circle cx="8" cy="8" r="7" fill="none" stroke="#3176b5" stroke-width="1"/><path d="M4.8 8.2l2.2 2.2 4.2-4.4" fill="none" stroke="#3176b5" stroke-width="1"/></svg><div><b>Personalized</b></div></li>
    <li style="top:120px"><svg viewBox="0 0 16 16"><circle cx="8" cy="8" r="7" fill="none" stroke="#3176b5" stroke-width="1"/><path d="M4.8 8.2l2.2 2.2 4.2-4.4" fill="none" stroke="#3176b5" stroke-width="1"/></svg><div><b>Transparency</b><span>Realtime updates</span></div></li>
    <li style="top:159px"><svg viewBox="0 0 16 16"><circle cx="8" cy="8" r="7" fill="none" stroke="#3176b5" stroke-width="1"/><path d="M4.8 8.2l2.2 2.2 4.2-4.4" fill="none" stroke="#3176b5" stroke-width="1"/></svg><div><b>Interactive</b><span>Ability to adapt, modify and change</span></div></li>
    <li style="top:198px"><svg viewBox="0 0 16 16"><circle cx="8" cy="8" r="7" fill="none" stroke="#3176b5" stroke-width="1"/><path d="M4.8 8.2l2.2 2.2 4.2-4.4" fill="none" stroke="#3176b5" stroke-width="1"/></svg><div><b>Speed</b><span>“I want it now”</span></div></li>
  </ul>
  <div class="target-photo" role="img" aria-label="Photo of arrows striking the centre of an archery target against a blurred city skyline"></div>
  <footer class="footer"><span>Copyright ©2019 Tolvenbrook Group Holdings Ltd. All rights reserved.</span><span>7</span></footer>
</section>

<section class="slide slide-8">
  <h2 class="slide-title">Technology to <strong>Enable Innovation</strong></h2>
  <div class="pillars">
    <div class="pillar">
      <div class="pillar-icon"><svg viewBox="0 0 44 44" fill="none" stroke="#3176b5" stroke-width="1.6"><rect x="2" y="2" width="38" height="38" rx="5"/><path d="M7 10l3 3 5-5M7 20l3 3 5-5M7 30l3 3 5-5M19 10h15M19 20h8"/><circle cx="33" cy="34" r="8" fill="#fff"/><path d="M33 29v5h4"/></svg></div>
      <div class="pillar-card"><h3>Data<br>Real Time</h3><ul><li>Streaming analytics</li><li>Federated data sources</li></ul></div>
    </div>
    <div class="pillar">
      <div class="pillar-icon"><svg viewBox="0 0 44 44" fill="none" stroke="#3176b5" stroke-width="1.6"><rect x="3" y="3" width="11" height="11" rx="1"/><rect x="30" y="3" width="11" height="11" rx="2"/><path d="M3 36l3-5h6l3 5-3 5H6z"/><circle cx="35" cy="36" r="6"/><path d="M14 8h16M8 14v17M35 14v16M15 36h14" stroke-dasharray="2 2"/></svg></div>
      <div class="pillar-card"><h3>Algorithms</h3><ul><li>Machine learning</li><li>Predictive analytics</li><li>Optimization</li></ul></div>
    </div>
    <div class="pillar">
      <div class="pillar-icon"><svg viewBox="0 0 44 44" fill="none" stroke="#3176b5" stroke-width="1.6"><path d="M2 14l8-8 6 6-8 8zM42 14l-8-8-6 6 8 8z"/><path d="M12 16l9-5 6 3-7 5c-2 1-4 0-3-2M14 19l12 12c2 2 5-1 3-3M18 25l7 7c2 2 4-1 2-3M15 28l6 6c2 2 4-1 2-3M13 31l4 4c2 2 4-1 2-3M30 18l3 10"/></svg></div>
      <div class="pillar-card"><h3>Collaboration</h3><ul><li>Machine to Machine</li><li>Organization to Organization</li><li>Internet of Things</li><li>Smart Cities</li></ul></div>
    </div>
    <div class="pillar">
      <div class="pillar-icon"><svg viewBox="0 0 44 44" fill="none" stroke="#3176b5" stroke-width="1.6"><path d="M19 2h6l1 5 4 2 4-3 4 4-3 4 2 4 5 1v6l-5 1-2 4 3 4-4 4-4-3-4 2-1 5h-6l-1-5-4-2-4 3-4-4 3-4-2-4-5-1v-6l5-1 2-4-3-4 4-4 4 3 4-2z"/><circle cx="22" cy="22" r="8"/><path d="M17 17a7 7 0 0 1 9-1"/></svg></div>
      <div class="pillar-card"><h3>Autonomous Operations</h3><ul><li>Self Driving vehicles</li><li>Self organizing machines</li></ul></div>
    </div>
    <div class="pillar">
      <div class="pillar-icon"><svg viewBox="0 0 44 44" fill="none" stroke="#3176b5" stroke-width="1.6"><rect x="2" y="2" width="40" height="40"/><path d="M2 8h40M5 5h1M8 5h1M11 5h1M8 14v-3h5M36 14v-3h-5M8 36v3h5M36 36v3h-5"/><circle cx="22" cy="25" r="4"/><path d="M22 16v3M22 31v3M13 25h3M28 25h3M16 19l2 2M26 29l2 2M28 19l-2 2M16 31l2-2"/></svg></div>
      <div class="pillar-card"><h3>User<br>Experience</h3><ul><li>Omni channel</li><li>Interactive</li><li>Convenient</li></ul></div>
    </div>
  </div>
  <footer class="footer"><span>Copyright ©2019 Tolvenbrook Group Holdings Ltd. All rights reserved.</span><span>8</span></footer>
</section>

<section class="slide slide-9">
  <h2 class="slide-title" style="top:18px">Final <strong>Thoughts</strong></h2>
  <div class="locker-photo" role="img" aria-label="Photo of a row of numbered parcel lockers with touchscreen kiosks and colourful panels"></div>
  <div class="thoughts">
    <div class="thought" style="left:0;width:202px"><svg viewBox="0 0 48 48" fill="none" stroke="#3176b5" stroke-width="1.6"><path d="M6 20v20h36V20M18 44h12M24 40v4M24 6v22M16 14v14M32 14v14M10 14h6M32 14h6"/><circle cx="24" cy="5" r="2"/><circle cx="9" cy="14" r="2"/><circle cx="39" cy="14" r="2"/></svg>Technology is available</div>
    <div class="divider" style="left:197px"></div>
    <div class="thought" style="left:197px;width:178px"><svg viewBox="0 0 48 48" fill="none" stroke="#3176b5" stroke-width="1.8"><circle cx="24" cy="24" r="17"/><circle cx="24" cy="24" r="10"/><path d="M24 2v14M24 32v14M2 24h14M32 24h14"/></svg>Focus on people and<br>experience</div>
    <div class="divider" style="left:375px"></div>
    <div class="thought" style="left:375px;width:190px"><svg viewBox="0 0 48 48" fill="none" stroke="#3176b5" stroke-width="1.6"><circle cx="24" cy="11" r="6"/><circle cx="11" cy="18" r="5"/><circle cx="37" cy="18" r="5"/><path d="M17 28c0-6 14-6 14 0M21 26v18h6V26M3 32c0-6 14-7 14-2M45 32c0-6-14-7-14-2"/></svg>Collaboration is critical</div>
  </div>
  <div class="credits"><a href="mailto:dana.morrell@tolvenbrook.com">Dana.Morrell@tolvenbrook.com</a><br>Photo: Ian Parrow</div>
  <footer class="footer"><span>Copyright ©2019 Tolvenbrook Group Holdings Ltd. All rights reserved.</span><span>9</span></footer>
</section>

<h1 class="part-heading">Second Part</h1>

</body>
</html>
```